Quillfern Litigation Funding Letterhead & Document Template

We need a letter head designed for our fund. Our fund works with law firms and investors across the globe. We need a a cover letter template as well as a document template for subsequent pages. Blue and white color scheme is preferred. This is our predecessor's website: https://www.quillfernlc.com/index.html. Please see our logo attached. The logo color code is #19478d. Font is Gotham-Medium.
Target Market(s)
Sophisticated investors and law firms
Font styles to use
Sans Serif
Colors
0255a3

```html
<!DOCTYPE html>
<html lang="en">
<head>
<meta charset="utf-8">
<title>Quillfern Litigation Funding — Letterhead</title>
<link rel="stylesheet" href="https://fonts.googleapis.com/css2?family=Montserrat:wght@500;600&family=Open+Sans:wght@400&display=swap">
<style>
  :root {
    --brand-blue: #19478d;
    --accent-blue: #0255a3;
    --backdrop: #dcdcde;
    --paper: #ffffff;
    --ink: #4a4a4a;
    --rule-grey: #b9b9bd;
    --edge-grey: #8e8e93;
  }
  * { box-sizing: border-box; margin: 0; padding: 0; }
  html, body { width: 1063px; height: 1200px; overflow: hidden; background: var(--backdrop); }
  .canvas { position: relative; width: 1063px; height: 1200px; }
  .letterhead {
    position: absolute; left: 122px; top: 22px; width: 820px; height: 1156px;
    background: var(--paper); box-shadow: 0 4px 18px rgba(0,0,0,.12);
    font-family: "Open Sans", Arial, sans-serif; color: var(--ink);
  }
  .brand {
    position: absolute; left: 70px; top: 112px; width: 330px;
    display: flex; align-items: center; gap: 12px;
  }
  .brand-square { width: 26px; height: 26px; background: var(--brand-blue); flex: none; }
  .brand-name {
    font-family: "Montserrat", Arial, sans-serif; font-weight: 600;
    font-size: 20px; line-height: 24px; letter-spacing: .5px; color: var(--brand-blue);
  }
  .contact {
    position: absolute; left: 480px; top: 72px;
    border-left: 1.5px solid var(--rule-grey); padding: 6px 0 6px 22px;
    font-family: "Montserrat", Arial, sans-serif; font-weight: 500; font-style: normal;
    font-size: 15px; line-height: 20px; color: var(--ink);
  }
  .contact-lines { list-style: none; margin-top: 2px; }
  .contact-lines li { display: flex; align-items: center; gap: 8px; padding-left: 12px; }
  .contact-lines svg { width: 14px; height: 14px; fill: var(--brand-blue); flex: none; }
  .letter-body {
    position: absolute; left: 100px; top: 300px; width: 600px;
    font-size: 14.5px; line-height: 21px;
  }
  .letter-body p { margin-bottom: 21px; }
  .signature-area {
    width: 130px; height: 90px; margin-top: 4px;
    background: linear-gradient(135deg, #f2f2f2, #e6e6e6); border-radius: 4px;
  }
  .footer { position: absolute; left: 0; bottom: 0; width: 820px; height: 80px; }
  .footer svg { display: block; }
  .footer-url {
    position: absolute; right: 40px; bottom: 22px;
    font-family: "Montserrat", Arial, sans-serif; font-weight: 500;
    font-size: 16px; color: #ffffff; letter-spacing: .3px;
  }
</style>
</head>
<body>
<main class="canvas">
  <article class="letterhead">
    <header>
      <div class="brand">
        <span class="brand-square"></span>
        <span class="brand-name">QUILLFERN LITIGATION<br>FUNDING</span>
      </div>
      <address class="contact">
        Larkmoor Plaza - Penthouse Floor<br>
        4180 Westhollow Avenue, Suite<br>
        1620 Houston, Texas 77046
        <ul class="contact-lines">
          <li><svg viewBox="0 0 24 24"><path d="M6.6 10.8a15 15 0 0 0 6.6 6.6l2.2-2.2a1 1 0 0 1 1-.25 11.4 11.4 0 0 0 3.6.57 1 1 0 0 1 1 1V20a1 1 0 0 1-1 1A17 17 0 0 1 3 4a1 1 0 0 1 1-1h3.5a1 1 0 0 1 1 1c0 1.25.2 2.45.57 3.57a1 1 0 0 1-.25 1z"/></svg>(713) 555-0142</li>
          <li><svg viewBox="0 0 24 24"><path d="M7 3h10v5H7zM4 9h16a2 2 0 0 1 2 2v6h-4v4H6v-4H2v-6a2 2 0 0 1 2-2zm4 7v3h8v-3z"/></svg>(713) 555-0187</li>
          <li><svg viewBox="0 0 24 24"><path d="M2 5h20v14H2zm2 2v.5l8 5 8-5V7l-8 5z"/></svg>info@quillfernlc.com</li>
        </ul>
      </address>
    </header>

    <section class="letter-body">
      <p>Dear customer,</p>
      <p>Lorem ipsum dolor sit amet, consectetur adipisicing elit, sed do eiusmod tempor incididunt ut labore et dolore magna aliqua. Ut enim ad minim veniam, quis nostrud exercitation ullamco laboris nisi ut aliquip ex ea commodo consequat. Duis aute irure dolor in reprehenderit in voluptate velit esse cillum dolore eu fugiat nulla pariatur. Excepteur sint occaecat cupidatat non proident, sunt in culpa qui officia deserunt mollit anim id est laborum.</p>
      <p>Lorem ipsum dolor sit amet, consectetur adipisicing elit, sed do eiusmod tempor incididunt ut labore et dolore magna aliqua. Ut enim ad minim veniam, quis nostrud exercitation ullamco laboris nisi ut aliquip ex ea commodo consequat. Duis aute irure dolor in reprehenderit in voluptate velit esse cillum dolore eu fugiat nulla pariatur. Excepteur sint occaecat cupidatat non proident, sunt in culpa qui officia deserunt mollit anim id est laborum.</p>
      <p>Lorem ipsum dolor sit amet, consectetur adipisicing elit, sed do eiusmod tempor incididunt ut labore et dolore magna aliqua. Ut enim ad minim veniam, quis nostrud exercitation ullamco laboris nisi ut aliquip ex ea commodo consequat. Duis aute irure dolor in reprehenderit in voluptate velit esse cillum dolore eu fugiat nulla pariatur. Excepteur sint occaecat cupidatat non proident, sunt in culpa qui officia deserunt mollit anim id est laborum.</p>
      <p>Lorem ipsum dolor sit amet, consectetur adipisicing elit, sed do eiusmod tempor incididunt ut labore et dolore magna aliqua. Ut enim ad minim veniam, quis nostrud exercitation ullamco laboris nisi ut aliquip ex ea commodo consequat. Duis aute irure dolor in reprehenderit.</p>
      <p>Yours Sincerely,</p>
      <div class="signature-area" role="img" aria-label="Handwritten signature of the sender"></div>
    </section>

    <footer class="footer">
      <svg width="820" height="80" viewBox="0 0 820 80" aria-hidden="true">
        <rect x="0" y="72" width="820" height="8" fill="var(--edge-grey)"/>
        <path d="M440 72 C468 72 470 60 478 44 C486 30 496 24 520 24 H820 V80 H440 Z" fill="var(--accent-blue)"/>
      </svg>
      <span class="footer-url">www.quillfernlc.com</span>
    </footer>
  </article>
</main>
</body>
</html>
```